Cardiology practice business card

We need a business card for our cardiology practice "Bellmoor Cardiology". We have a new logo, attached below. We like the colours in the logo - red and charcoal. The front of the business card will need to have the doctors name, address, phone number and email. The back will need to have space to write 2 appointment dates and times.

```html
<!DOCTYPE html>
<html lang="en">
<head>
<meta charset="utf-8">
<title>Bellmoor Cardiology – Business Card</title>
<link href="https://fonts.googleapis.com/css2?family=Red+Hat+Display:wght@400;500;700&display=swap" rel="stylesheet">
<style>
  :root{
    --red:#d1302b;
    --charcoal:#2b2b2e;
    --grey-band:#939598;
    --paper:#ffffff;
    --backdrop:#e4e2e3;
    --rule:#3a3a3d;
  }
  *{box-sizing:border-box;margin:0;padding:0}
  html,body{width:1200px;height:1108px;overflow:hidden}
  body{background:var(--backdrop);font-family:"Red Hat Display",sans-serif;color:var(--charcoal);position:relative}
  .card{position:absolute;left:228px;width:756px;background:var(--paper);border-radius:18px;overflow:hidden}
  .card--front{top:56px;height:461px}
  .card--back{top:575px;height:444px}
  .wordmark{position:absolute;display:flex;align-items:center;gap:14px;color:var(--red);font-weight:700;white-space:nowrap}
  .wordmark__dot{width:22px;height:22px;border-radius:50%;background:var(--red);flex:none}
  .card--front .wordmark{left:0;right:0;justify-content:center;top:124px;font-size:44px}
  .card--back .wordmark{right:50px;top:96px;font-size:34px}
  .band{position:absolute;left:0;top:0;width:756px;height:461px}
  .holder{position:absolute;right:410px;top:276px;text-align:right}
  .holder__name{color:var(--red);font-weight:700;font-size:31px;line-height:1}
  .holder__role{font-size:18px;margin-top:8px}
  .divider{position:absolute;left:381px;top:271px;width:2px;height:80px;background:var(--red)}
  .contacts{position:absolute;left:408px;top:268px;list-style:none}
  .contacts li{display:flex;align-items:center;gap:9px;font-size:18px;height:30.5px}
  .contacts svg{width:16px;height:16px;flex:none}
  .next-title{position:absolute;left:44px;top:212px;color:var(--red);font-weight:700;font-size:29px}
  .field{position:absolute;left:46px;right:51px;display:flex;align-items:flex-end;gap:3px;font-size:16px;font-weight:500}
  .field__line{flex:1;border-bottom:2px solid var(--rule);margin-bottom:3px}
  .field--time{top:290px}
  .field--date{top:374px}
</style>
</head>
<body>
  <section class="card card--front">
    <svg class="band" viewBox="0 0 756 461" aria-hidden="true">
      <path d="M0 350 Q378 450 756 343 L756 461 L0 461 Z" fill="var(--grey-band)"/>
      <path d="M83 355 Q378 430 690 355" fill="none" stroke="var(--red)" stroke-width="4"/>
    </svg>
    <div class="wordmark"><span class="wordmark__dot"></span>Bellmoor Cardiology</div>
    <div class="holder">
      <p class="holder__name">Daniel Hart</p>
      <p class="holder__role">Managing Director</p>
    </div>
    <div class="divider"></div>
    <ul class="contacts">
      <li><svg viewBox="0 0 16 16"><path d="M3 1.5l3 3-1.6 1.8c.9 2 2.3 3.4 4.3 4.3L10.5 9l3 3-1.8 2.2C6.5 14 2 9.5 1.8 3.3z" fill="var(--red)"/></svg>555-014-0188</li>
      <li><svg viewBox="0 0 16 16"><rect x="1.5" y="3.5" width="13" height="9" rx="1" fill="var(--red)"/><path d="M1.8 4l6.2 4.6L14.2 4" fill="none" stroke="#fff" stroke-width="1.3"/></svg>info@bellmoorcardiology.com</li>
      <li><svg viewBox="0 0 16 16"><circle cx="8" cy="8" r="6.8" fill="var(--red)"/><path d="M1.5 8h13M8 1.2c2.2 2 2.2 11.6 0 13.6M8 1.2c-2.2 2-2.2 11.6 0 13.6" fill="none" stroke="#fff" stroke-width="1"/></svg>www.bellmoorcardiology.com</li>
    </ul>
  </section>

  <section class="card card--back">
    <div class="wordmark"><span class="wordmark__dot"></span>Bellmoor Cardiology</div>
    <h2 class="next-title">Next Apointment</h2>
    <div class="field field--time"><span>Time:</span><span class="field__line"></span></div>
    <div class="field field--date"><span>Date:</span><span class="field__line"></span></div>
  </section>
</body>
</html>
```